Wholesale Janitorial supply company needs promotional postcard

We need a postcard designed to entice old customers who stopped buying their janitorial and maintenance supplies( cleaning chemicals, paper supplies, etc) from us. We wanted a "we missed you" type theme, offering a 15% discount on your next order of $300.00 or more. Colors are green with black and white accents. Our website is quorvia.com, it will give you a better understanding of exactly who we are.

Industry/Entity Type

It Company

Font styles to use
Sans Serif

```html
<!DOCTYPE html>
<html lang="en">
<head>
<meta charset="utf-8">
<title>Quorvia Supply – We Missed You Postcard</title>
<link href="https://fonts.googleapis.com/css2?family=Open+Sans:wght@400;600;700&family=Noto+Sans:wght@400;700&display=swap" rel="stylesheet">
<style>
  :root {
    --green: #23b14b;
    --green-dark: #077a4b;
    --white: #ffffff;
    --ink: #111111;
  }
  * { margin: 0; padding: 0; box-sizing: border-box; }
  html, body { width: 1200px; height: 1000px; overflow: hidden; background: var(--white); }
  .canvas { position: relative; width: 1200px; height: 1000px; font-family: "Open Sans", sans-serif; }

  .block { position: absolute; }
  .headline-band { left: 158px; top: 344px; width: 403px; height: 91px; background: var(--green); }
  .headline {
    position: absolute; left: 18px; top: 16px;
    color: var(--white); font-size: 49px; font-weight: 400; letter-spacing: 0.5px; white-space: nowrap;
  }
  .offer-box { left: 158px; top: 442px; width: 197px; height: 118px; background: var(--green-dark); color: var(--white); }
  .offer-percent { position: absolute; left: 36px; top: -8px; font-size: 88px; font-weight: 400; letter-spacing: -5px; line-height: 1; }
  .offer-label { position: absolute; left: 22px; top: 74px; font-size: 36px; letter-spacing: 1px; line-height: 1; }

  .accent-square { left: 365px; top: 473px; width: 125px; height: 113px; background: var(--green); }
  .brand-box { left: 414px; top: 546px; width: 154px; height: 124px; background: var(--white); }
  .brand-box-inner { position: absolute; left: 7px; top: 7px; width: 140px; height: 109px; background: var(--green-dark); }
  .brand-plate {
    position: absolute; left: 7px; top: 34px; width: 120px; height: 34px; background: var(--white);
    display: flex; align-items: center; justify-content: center;
    color: var(--green-dark); font-size: 15px; font-weight: 600; white-space: nowrap;
  }

  .back-art { position: absolute; left: 627px; top: 344px; width: 194px; height: 312px; }
  .back-message {
    position: absolute; left: 636px; top: 441px; width: 190px;
    color: var(--white); font-family: "Noto Sans", sans-serif; font-size: 10.2px; line-height: 11.6px; white-space: nowrap;
  }
  .contact {
    position: absolute; left: 827px; top: 363px;
    color: var(--ink); font-family: "Noto Sans", sans-serif; font-size: 5.4px; font-weight: 700; line-height: 6px; white-space: nowrap;
  }
</style>
</head>
<body>
<div class="canvas">
  <section class="front">
    <div class="block headline-band"><h1 class="headline">We missed you!</h1></div>
    <div class="block offer-box">
      <span class="offer-percent">15%</span>
      <span class="offer-label">discount</span>
    </div>
    <div class="block accent-square"></div>
    <div class="block brand-box">
      <div class="brand-box-inner">
        <div class="brand-plate">Quorvia Supply</div>
      </div>
    </div>
  </section>

  <section class="back">
    <svg class="back-art" viewBox="0 0 194 312" width="194" height="312" aria-hidden="true">
      <rect width="194" height="312" fill="#23b14b"/>
      <g fill="#ffffff">
        <rect x="51" y="0" width="7" height="91"/>
        <rect x="0" y="84" width="58" height="7"/>
        <rect x="109" y="0" width="7" height="76"/>
        <rect x="109" y="69" width="85" height="7"/>
        <rect x="0" y="192" width="96" height="7"/>
        <rect x="89" y="192" width="7" height="62"/>
        <rect x="0" y="247" width="96" height="7"/>
        <rect x="112" y="206" width="7" height="106"/>
        <rect x="112" y="207" width="82" height="7"/>
        <rect x="159" y="176" width="6" height="36"/>
        <rect x="159" y="176" width="35" height="4"/>
      </g>
    </svg>
    <p class="back-message">We're missing you always buy<br>your cleaning chemicals and supplies.<br>We miss you for that reason we are<br>offering a 15% discount on your<br>next order of $ 300.00 or more.<br>and remember in Quorvia Supply<br>WE MISS YOU!</p>
    <p class="contact">118 Birchfield Road, Larkton, NJ 07412<br>&nbsp;phone #800 555-0147<br>website quorvia.com</p>
  </section>
</div>
</body>
</html>
```